Business Card Design

My focus is upon the over 75s, for whom I designed a specialised massage technique (I am qualified as a naturopath). The title is a play on the Japanese words for 'red', and for 'person' (I'm ethnically Australian, but am from Japan), and mirrors the Japanese word for 'baby' (miss/master red). There should be plenty of red used in the card, and, if possible, reflect vitality, vigour, vibrancy, without being garish, harsh, or too bright.

Target Market(s)

All ages, but specifically the over 75s.

Industry/Entity Type

Massage

Contact Information for Business Card

Tolu-ve
Mobile Massage
0487206143
Relax, Deep Tissue, Facials
Custom-Designed Massage for the over 75s
Locals and Seniors (75+) Discounts

```html
<!DOCTYPE html>
<html lang="en">
<head>
<meta charset="utf-8">
<title>Tolu-ve Mobile Massage – Business Card</title>
<link rel="stylesheet" href="https://fonts.googleapis.com/css2?family=Roboto:wght@300;400;700&display=swap">
<style>
  :root {
    --brand-red: #e5332a;
    --figure-tint: #f07a6e;
    --card-bg: #ffffff;
  }
  html, body {
    margin: 0;
    padding: 0;
    width: 1200px;
    height: 741px;
    overflow: hidden;
    background: var(--card-bg);
  }
  .card {
    position: relative;
    width: 1200px;
    height: 741px;
    background: var(--card-bg);
    font-family: "Roboto", Helvetica, Arial, sans-serif;
    color: var(--brand-red);
  }
  .mascot-area {
    position: absolute;
    left: 680px;
    top: 160px;
    width: 112px;
    height: 180px;
  }
  .brand-name {
    position: absolute;
    left: 0;
    width: 1270px;
    top: 320px;
    margin: 0;
    text-align: center;
    font-weight: 400;
    font-size: 140px;
    line-height: 140px;
    letter-spacing: -1px;
  }
  .brand-tagline {
    position: absolute;
    left: 0;
    width: 1264px;
    top: 462px;
    margin: 0;
    text-align: center;
    font-weight: 400;
    font-size: 72px;
    line-height: 72px;
  }
  .services {
    position: absolute;
    left: 0;
    width: 1194px;
    top: 554px;
    margin: 0;
    text-align: center;
    font-weight: 300;
    font-size: 32px;
    line-height: 54px;
  }
  .services .phone {
    font-weight: 700;
  }
</style>
</head>
<body>
  <main class="card">
    <svg class="mascot-area" viewBox="0 0 112 180" role="img" aria-label="Brand mascot: a small red dancing figure">
      <rect x="0" y="0" width="112" height="180" rx="14" fill="var(--figure-tint)" opacity="0.35"/>
    </svg>
    <h1 class="brand-name">Tolu-ve</h1>
    <p class="brand-tagline">Mobile Massage</p>
    <p class="services">
      Relax, Deep Tissue, Facials Custom-Designed Massage<br>
      for the over 75s Locals and Seniors (75+) Discounts<br>
      Call <span class="phone">0487 206 143</span>
    </p>
  </main>
</body>
</html>
```